Plastic Jar Catalogue 7

We are a plastic factory manufacturing different size of plastic jars, which mostly use for spice and grinded coffee. I need the catalogue to be 3 pages:First page: an attractive cover shows the factory's name and logo with a space for products’ picture. Second page: is an items page which I prefer to be enough for 4 items with a space for item number and description under each item. Last page: to be for factory’s address and contact details.

```html
<!DOCTYPE html>
<html lang="en">
<head>
<meta charset="utf-8">
<title>Clearwell Plastic Works – Jar Catalogue</title>
<link href="https://fonts.googleapis.com/css2?family=Oswald:wght@500&family=Source+Sans+3:wght@400;600;700&display=swap" rel="stylesheet">
<style>
  :root{
    --backdrop:#6e6d72;
    --paper:#ffffff;
    --teal:#1f96b2;
    --ink:#1a1a1a;
    --jar-light:#f4f6f7;
    --jar-mid:#d9dee1;
  }
  *{margin:0;padding:0;box-sizing:border-box}
  html,body{width:1200px;height:960px;overflow:hidden;background:var(--backdrop)}
  .canvas{position:relative;width:1200px;height:960px}
  .page{position:absolute;width:368px;height:519px;background:var(--paper);overflow:hidden}
  .page--cover{left:30px;top:218px}
  .page--items{left:414px;top:222px}
  .page--contact{left:802px;top:218px}
  .band{position:absolute;left:0;width:100%;height:10px;background:var(--teal)}
  .band--top{top:0}
  .band--bottom{bottom:0}
  .block{position:absolute;background:var(--teal)}
  .photo{position:absolute;background:radial-gradient(ellipse at 50% 45%,var(--jar-light) 0%,var(--jar-mid) 100%)}
  .frame{position:absolute;border:4px solid var(--teal);background:var(--paper);padding:6px}
  .frame .photo{position:static;width:100%;height:100%}

  .wordmark{position:absolute;display:flex;align-items:center;gap:8px;
    font-family:"Source Sans 3",sans-serif;font-weight:600;color:var(--ink);
    text-transform:uppercase;line-height:1.15;text-align:center}
  .wordmark__square{background:var(--teal);flex:none}
  .wordmark--cover{left:0;width:100%;top:52px;justify-content:center;font-size:17px;letter-spacing:3px}
  .wordmark--cover .wordmark__square{width:30px;height:30px}
  .wordmark--footer{left:240px;top:442px;font-size:9px;letter-spacing:1.6px;gap:6px}
  .wordmark--footer .wordmark__square{width:14px;height:14px}

  .cover-title{position:absolute;left:0;width:100%;top:438px;text-align:center;white-space:nowrap;
    font-family:"Oswald",sans-serif;font-weight:500;font-size:30px;color:var(--teal);
    text-transform:uppercase;letter-spacing:0.2px;line-height:1}

  .item{position:absolute;left:22px;width:330px;height:88px}
  .item .frame{left:0;top:0;width:88px;height:88px;border-width:3px;padding:5px}
  .item__body{position:absolute;left:100px;top:-2px;width:222px}
  .item__title{font-family:"Source Sans 3",sans-serif;font-weight:700;font-size:14.5px;color:var(--teal);line-height:1.2;margin-bottom:4px}
  .item__text{font-family:"Source Sans 3",sans-serif;font-weight:600;font-size:6.8px;line-height:8.8px;color:var(--ink);text-align:justify}

  .contact{position:absolute;left:0;top:277px;width:100%;height:117px;background:var(--teal);
    padding:18px 30px;color:var(--paper);font-family:"Source Sans 3",sans-serif}
  .contact__heading{font-family:"Oswald",sans-serif;font-weight:500;font-size:16px;letter-spacing:0.5px;
    text-transform:uppercase;line-height:1;margin-bottom:10px}
  .contact__list{list-style:none}
  .contact__row{display:flex;align-items:center;gap:8px;font-size:10.5px;font-weight:400;line-height:1;margin-bottom:7px}
  .contact__icon{width:11px;height:11px;flex:none;fill:none;stroke:var(--paper);stroke-width:1.6;stroke-linecap:round;stroke-linejoin:round}
</style>
</head>
<body>
<div class="canvas">

  <section class="page page--cover">
    <div class="band band--top"></div>
    <div class="wordmark wordmark--cover">
      <span class="wordmark__square"></span>
      <span>Clearwell<br>Plastic Works</span>
    </div>
    <div class="block" style="left:0;top:155px;width:63px;height:117px"></div>
    <div class="frame" style="left:72px;top:155px;width:116px;height:116px">
      <div class="photo" role="img" aria-label="Clear plastic jar with silver metal lid"></div>
    </div>
    <div class="photo" style="left:214px;top:166px;width:88px;height:88px" role="img" aria-label="Wide clear plastic jar with white screw cap"></div>
    <div class="photo" style="left:74px;top:286px;width:80px;height:100px" role="img" aria-label="Clear plastic jar with white cap"></div>
    <div class="frame" style="left:181px;top:278px;width:116px;height:116px">
      <div class="photo" role="img" aria-label="Clear plastic jar beside its white lid"></div>
    </div>
    <div class="block" style="left:305px;top:277px;width:63px;height:118px"></div>
    <h1 class="cover-title">Clearwell Plastic Works</h1>
    <div class="band band--bottom"></div>
  </section>

  <section class="page page--items">
    <div class="band band--top" style="height:11px"></div>

    <article class="item" style="top:52px">
      <div class="frame"><div class="photo" role="img" aria-label="Clear jar with silver metal lid"></div></div>
      <div class="item__body">
        <h2 class="item__title">Title Lorem Ipsum</h2>
        <p class="item__text">"Lorem ipsum dolor sit amet, consectetur adipiscing elit, sed do eiusmod tempor incididunt ut labore et dolore magna aliqua. Ut enim ad minim veniam, quis nostrud exercitation ullamco laboris nisi ut aliquip ex ea commodo consequat. Duis aute irure dolor in reprehenderit in voluptate velit esse cillum dolore eu fugiat nulla pariatur. Excepteur sint occaecat cupidatat non proident, sunt in culpa qui officia deserunt mollit anim id est laborum."</p>
      </div>
    </article>

    <article class="item" style="top:162px">
      <div class="frame"><div class="photo" role="img" aria-label="Wide clear jar with white cap"></div></div>
      <div class="item__body">
        <h2 class="item__title">Title Lorem Ipsum</h2>
        <p class="item__text">"Lorem ipsum dolor sit amet, consectetur adipiscing elit, sed do eiusmod tempor incididunt ut labore et dolore magna aliqua. Ut enim ad minim veniam, quis nostrud exercitation ullamco laboris nisi ut aliquip ex ea commodo consequat. Duis aute irure dolor in reprehenderit in voluptate velit esse cillum dolore eu fugiat nulla pariatur. Excepteur sint occaecat cupidatat non proident, sunt in culpa qui officia deserunt mollit anim id est laborum."</p>
      </div>
    </article>

    <article class="item" style="top:273px">
      <div class="frame"><div class="photo" role="img" aria-label="Clear jar with white lid set aside"></div></div>
      <div class="item__body">
        <h2 class="item__title">Title Lorem Ipsum</h2>
        <p class="item__text">"Lorem ipsum dolor sit amet, consectetur adipiscing elit, sed do eiusmod tempor incididunt ut labore et dolore magna aliqua. Ut enim ad minim veniam, quis nostrud exercitation ullamco laboris nisi ut aliquip ex ea commodo consequat. Duis aute irure dolor in reprehenderit in voluptate velit esse cillum dolore eu fugiat nulla pariatur. Excepteur sint occaecat cupidatat non proident, sunt in culpa qui officia deserunt mollit anim id est laborum."</p>
      </div>
    </article>

    <article class="item" style="top:382px">
      <div class="frame"><div class="photo" role="img" aria-label="Small clear jar with white cap"></div></div>
      <div class="item__body">
        <h2 class="item__title">Title Lorem Ipsum</h2>
        <p class="item__text">"Lorem ipsum dolor sit amet, consectetur adipiscing elit, sed do eiusmod tempor incididunt ut labore et dolore magna aliqua. Ut enim ad minim veniam, quis nostrud exercitation ullamco laboris nisi ut aliquip ex ea commodo consequat. Duis aute irure dolor in reprehenderit in voluptate velit esse cillum dolore eu fugiat nulla pariatur. Excepteur sint occaecat cupidatat non proident, sunt in culpa qui officia deserunt mollit anim id est laborum."</p>
      </div>
    </article>

    <div class="band band--bottom" style="height:11px"></div>
  </section>

  <section class="page page--contact">
    <div class="band band--top"></div>
    <div class="photo" style="left:58px;top:86px;width:254px;height:138px" role="img" aria-label="Group of tall clear plastic jars with black caps"></div>
    <div class="contact">
      <h2 class="contact__heading">Contact Us</h2>
      <ul class="contact__list">
        <li class="contact__row">
          <svg class="contact__icon" viewBox="0 0 12 12" aria-hidden="true"><path d="M6 11s4-3.8 4-6.6A4 4 0 0 0 2 4.4C2 7.2 6 11 6 11z"/><circle cx="6" cy="4.5" r="1.3"/></svg>
          <span>14 Harbor Road, Unit 7, Eastfield Industrial Zone</span>
        </li>
        <li class="contact__row">
          <svg class="contact__icon" viewBox="0 0 12 12" aria-hidden="true"><path d="M2.5 1.5h2l1 2.5-1.3.9a6 6 0 0 0 2.9 2.9l.9-1.3 2.5 1v2a1 1 0 0 1-1 1A8.5 8.5 0 0 1 1.5 2.5a1 1 0 0 1 1-1z"/></svg>
          <span>+1 555 0142 880</span>
        </li>
        <li class="contact__row">
          <svg class="contact__icon" viewBox="0 0 12 12" aria-hidden="true"><rect x="1" y="2.5" width="10" height="7" rx="1"/><path d="M1.3 3l4.7 3.6L10.7 3"/></svg>
          <span>sales@clearwellplastic.example</span>
        </li>
        <li class="contact__row">
          <svg class="contact__icon" viewBox="0 0 12 12" aria-hidden="true"><circle cx="6" cy="6" r="4.8"/><path d="M1.2 6h9.6M6 1.2c1.6 1.5 1.6 8.1 0 9.6M6 1.2c-1.6 1.5-1.6 8.1 0 9.6"/></svg>
          <span>www.clearwellplastic.example</span>
        </li>
      </ul>
    </div>
    <div class="wordmark wordmark--footer">
      <span class="wordmark__square"></span>
      <span>Clearwell<br>Plastic Works</span>
    </div>
    <div class="band band--bottom"></div>
  </section>

</div>
</body>
</html>
```